roofing door hanger

we would like to have our logo kvt roofing, it would be given when we are working in the neighborhood and have our services roof replacement, roof repair, ventilation, inspections. Our slogan is "Reliability starts at the top" . Our company is kvt roofing i would like to get one or two reviews from google, and f any pictures are needed can use facebook.

Industry/Entity Type

Roofing

Requirements
Must have
• this has to be a door hanger design

```html
<!DOCTYPE html>
<html lang="en">
<head>
<meta charset="utf-8">
<title>KVT Roofing – Door Hangers</title>
<link rel="stylesheet" href="https://fonts.googleapis.com/css2?family=Michroma&family=Saira+Semi+Condensed:wght@600;700&family=Lato:ital,wght@1,400;1,700&display=swap">
<style>
  :root{
    --bg:#ebe9e6;
    --orange:#f58220;
    --charcoal:#3a3b3d;
    --dark:#222326;
    --black:#0d0d0d;
    --white:#ffffff;
  }
  html,body{margin:0;padding:0;overflow:hidden;}
  body{width:1200px;height:960px;background:var(--bg);position:relative;}
  .defs{position:absolute;width:0;height:0;}
  .hanger{position:absolute;top:109px;width:279px;height:723px;display:block;
    filter:drop-shadow(2px 3px 3px rgba(0,0,0,.35));}
  .hanger--1{left:26px}.hanger--2{left:315px}.hanger--3{left:604px}.hanger--4{left:893px}
  .headline{font-family:"Saira Semi Condensed",sans-serif;font-weight:700;font-style:italic;}
  .wide{font-family:"Michroma",sans-serif;}
  .review{font-family:"Lato",sans-serif;font-style:italic;font-size:9.4px;fill:var(--white);}
  .reviewer{font-family:"Lato",sans-serif;font-style:italic;font-weight:700;font-size:9.4px;fill:var(--orange);}
  .stars{fill:var(--orange);}
</style>
</head>
<body>

<svg class="defs" aria-hidden="true">
  <defs>
    <linearGradient id="tools-shot" x1="0" y1="0" x2="0" y2="1">
      <stop offset="0" stop-color="#2a2a2c"/>
      <stop offset=".5" stop-color="#3b3734"/>
      <stop offset="1" stop-color="#1c1c1e"/>
    </linearGradient>
    <linearGradient id="photo-tudor" x1="0" y1="0" x2="0" y2="1">
      <stop offset="0" stop-color="#b9bcc0"/><stop offset=".35" stop-color="#6f5243"/>
      <stop offset=".7" stop-color="#8a6a3a"/><stop offset="1" stop-color="#b48a3a"/>
    </linearGradient>
    <linearGradient id="photo-green-roof" x1="0" y1="0" x2="0" y2="1">
      <stop offset="0" stop-color="#cfd2d4"/><stop offset=".35" stop-color="#3f5a4e"/>
      <stop offset=".7" stop-color="#e6dfc6"/><stop offset="1" stop-color="#9d9c97"/>
    </linearGradient>
    <linearGradient id="photo-gray-roof" x1="0" y1="0" x2="0" y2="1">
      <stop offset="0" stop-color="#d6d8da"/><stop offset=".4" stop-color="#6b6e75"/>
      <stop offset=".7" stop-color="#e4e1d8"/><stop offset="1" stop-color="#4f7a38"/>
    </linearGradient>
    <linearGradient id="photo-colonial" x1="0" y1="0" x2="0" y2="1">
      <stop offset="0" stop-color="#c9cfd2"/><stop offset=".35" stop-color="#5b6a55"/>
      <stop offset=".65" stop-color="#e8e8e4"/><stop offset="1" stop-color="#4c7f32"/>
    </linearGradient>

    <symbol id="hanger-body" viewBox="0 0 279 723">
      <rect width="279" height="723" fill="var(--orange)"/>
      <path d="M0,124 C50,100 90,88 140,84 L279,72 L279,88 L140,99 C90,103 50,116 0,140 Z" fill="var(--black)"/>
      <path d="M0,426 C55,422 88,405 100,372 C110,340 116,308 143,292 C173,276 225,270 279,264 L279,723 L0,723 Z" fill="var(--charcoal)"/>
      <path d="M0,506 L279,462 L279,508 C170,524 70,540 38,580 C20,604 14,650 14,723 L0,723 Z" fill="var(--orange)"/>
      <path d="M279,508 C170,524 70,540 38,580 C20,604 14,650 14,723 L279,723 Z" fill="url(#tools-shot)" role="img" aria-label="Photo of roofing tools and shingles"/>
      <circle cx="140" cy="69" r="45" fill="var(--bg)"/>
    </symbol>

    <symbol id="stars" viewBox="0 0 80 12">
      <g class="stars">
        <polygon points="6,0 7.6,4.2 12,4.4 8.5,7.2 9.7,11.5 6,9 2.3,11.5 3.5,7.2 0,4.4 4.4,4.2"/>
        <polygon transform="translate(17,0)" points="6,0 7.6,4.2 12,4.4 8.5,7.2 9.7,11.5 6,9 2.3,11.5 3.5,7.2 0,4.4 4.4,4.2"/>
        <polygon transform="translate(34,0)" points="6,0 7.6,4.2 12,4.4 8.5,7.2 9.7,11.5 6,9 2.3,11.5 3.5,7.2 0,4.4 4.4,4.2"/>
        <polygon transform="translate(51,0)" points="6,0 7.6,4.2 12,4.4 8.5,7.2 9.7,11.5 6,9 2.3,11.5 3.5,7.2 0,4.4 4.4,4.2"/>
        <polygon transform="translate(68,0)" points="6,0 7.6,4.2 12,4.4 8.5,7.2 9.7,11.5 6,9 2.3,11.5 3.5,7.2 0,4.4 4.4,4.2"/>
      </g>
    </symbol>

    <symbol id="reviews" viewBox="0 0 279 723">
      <use href="#stars" x="181" y="536" width="76" height="12"/>
      <text class="review" text-anchor="end">
        <tspan x="257" y="566">“So incredibly impressed with how fast</tspan>
        <tspan x="257" y="578">they were able to come to my home to tarp it off after</tspan>
        <tspan x="257" y="590">the wind storm over the weekend. The two men working</tspan>
        <tspan x="257" y="602">on our home were so happy to help and wonderful to</tspan>
        <tspan x="257" y="614">work with! Thank you!”</tspan>
      </text>
      <text class="reviewer" x="257" y="630" text-anchor="end">Marissa T.</text>
      <text class="review" text-anchor="end">
        <tspan x="257" y="655">“We were impressed with KVT Roofing from beginning to</tspan>
        <tspan x="257" y="667">end. They were easy to work with, professional, and did</tspan>
        <tspan x="257" y="679">a wonderful job. Our new roof looks amazing.”</tspan>
      </text>
      <text class="reviewer" x="257" y="695" text-anchor="end">Dana R.</text>
    </symbol>

    <symbol id="phone" viewBox="0 0 279 723">
      <text class="wide" transform="translate(27,530) rotate(-8.6) skewX(-14)" fill="var(--black)" textLength="228" lengthAdjust="spacingAndGlyphs">
        <tspan font-size="14">555</tspan><tspan font-size="25" dx="2">318.4407</tspan>
      </text>
    </symbol>

    <path id="photo-area" d="M0,168 C40,138 80,122 140,118 L279,108 L279,250 C222,255 172,260 142,272 C112,286 100,320 90,350 C80,385 50,404 0,410 Z"/>
  </defs>
</svg>

<!-- Hanger 1 -->
<svg class="hanger hanger--1" viewBox="0 0 279 723" aria-label="KVT Roofing door hanger">
  <use href="#hanger-body"/>
  <use href="#photo-area" fill="url(#photo-tudor)" role="img" aria-label="Photo of a brick Tudor-style house with a new roof and autumn lawn"/>
  <g class="headline" transform="rotate(-7 258 382)" font-size="25">
    <text x="118" y="354" fill="var(--orange)" textLength="140" lengthAdjust="spacingAndGlyphs">CALL US TODAY</text>
    <text x="154" y="382" fill="var(--white)" textLength="104" lengthAdjust="spacingAndGlyphs">FOR THE NO</text>
    <text x="134" y="410" fill="var(--white)" textLength="124" lengthAdjust="spacingAndGlyphs">B.S ESTIMATE</text>
  </g>
  <text class="wide" transform="translate(29,482) rotate(-8.6) skewX(-12)" font-size="15" fill="var(--white)" textLength="226" lengthAdjust="spacingAndGlyphs">KVT-ROOFING.COM</text>
  <use href="#phone"/>
  <use href="#reviews"/>
</svg>

<!-- Hanger 2 -->
<svg class="hanger hanger--2" viewBox="0 0 279 723" aria-label="KVT Roofing door hanger">
  <use href="#hanger-body"/>
  <use href="#photo-area" fill="url(#photo-green-roof)" role="img" aria-label="Photo of a cream-sided house with a new green shingle roof and porch"/>
  <g class="headline" transform="rotate(-7 258 376)" font-size="44">
    <text x="138" y="350" fill="var(--orange)" textLength="120" lengthAdjust="spacingAndGlyphs">CALL US</text>
    <text x="138" y="402" fill="var(--orange)" textLength="120" lengthAdjust="spacingAndGlyphs">TODAY</text>
  </g>
  <text class="headline" transform="translate(29,456) rotate(-8.6)" font-size="22" fill="var(--white)" textLength="226" lengthAdjust="spacingAndGlyphs">FOR THE NO B.S ESTIMATE</text>
  <text class="wide" transform="translate(29,486) rotate(-8.6) skewX(-12)" font-size="15" fill="var(--orange)" textLength="226" lengthAdjust="spacingAndGlyphs">KVT-ROOFING.COM</text>
  <use href="#phone"/>
  <use href="#reviews"/>
</svg>

<!-- Hanger 3 -->
<svg class="hanger hanger--3" viewBox="0 0 279 723" aria-label="KVT Roofing door hanger">
  <use href="#hanger-body"/>
  <use href="#photo-area" fill="url(#photo-gray-roof)" role="img" aria-label="Photo of a white house with a new gray roof and a roofer on a ladder"/>
  <g class="headline" transform="rotate(-7 258 382)" font-size="25">
    <text x="118" y="354" fill="var(--orange)" textLength="140" lengthAdjust="spacingAndGlyphs">CALL US TODAY</text>
    <text x="154" y="382" fill="var(--white)" textLength="104" lengthAdjust="spacingAndGlyphs">FOR THE NO</text>
    <text x="134" y="410" fill="var(--white)" textLength="124" lengthAdjust="spacingAndGlyphs">B.S ESTIMATE</text>
  </g>
  <text class="wide" transform="translate(29,486) rotate(-8.6) skewX(-12)" font-size="15" fill="var(--orange)" textLength="226" lengthAdjust="spacingAndGlyphs">KVT-ROOFING.COM</text>
  <use href="#phone"/>
  <use href="#reviews"/>
</svg>

<!-- Hanger 4 -->
<svg class="hanger hanger--4" viewBox="0 0 279 723" aria-label="KVT Roofing door hanger">
  <use href="#hanger-body"/>
  <use href="#photo-area" fill="url(#photo-colonial)" role="img" aria-label="Photo of a two-story brick and white colonial house with a ladder against the roof"/>
  <g class="headline" transform="rotate(-7 258 376)" font-size="44">
    <text x="138" y="350" fill="var(--orange)" textLength="120" lengthAdjust="spacingAndGlyphs">CALL US</text>
    <text x="138" y="402" fill="var(--orange)" textLength="120" lengthAdjust="spacingAndGlyphs">TODAY</text>
  </g>
  <text class="wide" transform="translate(29,458) rotate(-8.6) skewX(-12)" font-size="10.5" fill="var(--white)" textLength="226" lengthAdjust="spacingAndGlyphs">FOR THE NO B.S ESTIMATE</text>
  <text class="wide" transform="translate(29,484) rotate(-8.6) skewX(-12)" font-size="15" fill="var(--orange)" textLength="226" lengthAdjust="spacingAndGlyphs">KVT-ROOFING.COM</text>
  <use href="#phone"/>
  <use href="#reviews"/>
</svg>

</body>
</html>
```